Podcast cover design for a new podcast called 'Formosan Trail Blazers'

I would like a clean, professional and impactful design for a new podcast I am launching called 'Formosan Trail Blazers'. 'Formosan Trail Blazers,' is a podcast featuring conversations with the island's groundbreaking entrepreneurs, technologists, artists, and scientists. Each episode uncovers the stories and insights of visionaries who are shaping Taiwan's future through cutting-edge startups, technological breakthroughs, artistic innovation, and scientific discovery. The podcast cover needs to look professional and be impactful. Ideally, I would also like the podcast cover to feature an photo or image of myself. Please see uploaded two recent photos of myself which you can crop etc for the podcast cover.

```html
<!DOCTYPE html>
<html lang="en">
<head>
<meta charset="utf-8">
<title>Formosan Trail Blazers — Podcast Cover</title>
<link href="https://fonts.googleapis.com/css2?family=Montserrat:wght@500;800&family=Oswald:wght@500&display=swap" rel="stylesheet">
<style>
  :root {
    --lime: #a9be3b;
    --ink: #25262b;
    --paper: #ffffff;
    --grid: #ebebeb;
    --photo-top: #c89a7e;
    --photo-mid: #2b2d33;
    --photo-low: #9dc45a;
  }
  * { margin: 0; padding: 0; box-sizing: border-box; }
  html, body { width: 1200px; height: 1200px; overflow: hidden; background: var(--paper); }
  .cover {
    position: relative;
    width: 1200px;
    height: 1200px;
    overflow: hidden;
    background-color: var(--paper);
    background-image:
      linear-gradient(to right, var(--grid) 2px, transparent 2px),
      linear-gradient(to bottom, var(--grid) 2px, transparent 2px);
    background-size: 97px 66px;
    background-position: 68px 40px;
  }
  .cover-art, .host-photo { position: absolute; left: 0; top: 0; }
  .show-title {
    position: absolute;
    left: 0;
    width: 630px;
    top: 316px;
    text-align: center;
    font-family: "Montserrat", sans-serif;
    z-index: 2;
  }
  .show-title__main {
    display: block;
    font-weight: 800;
    font-size: 86px;
    line-height: 1;
    letter-spacing: 1px;
    color: var(--lime);
  }
  .show-title__sub {
    display: block;
    margin-top: 16px;
    font-weight: 500;
    font-size: 38px;
    line-height: 1;
    letter-spacing: 1px;
    color: var(--ink);
  }
</style>
</head>
<body>
<main class="cover">
  <svg class="cover-art" width="1200" height="1200" viewBox="0 0 1200 1200" aria-hidden="true">
    <defs>
      <clipPath id="canvas-clip"><rect width="1200" height="1200"/></clipPath>
    </defs>
    <g clip-path="url(#canvas-clip)">
      <circle class="corner-accent" cx="0" cy="0" r="109" fill="var(--lime)"/>
      <path class="accent-ring" fill="var(--lime)" fill-rule="evenodd"
        d="M900 1016 m-590 0 a590 590 0 1 0 1180 0 a590 590 0 1 0 -1180 0 Z
           M900 1016 m-440 0 a440 440 0 1 0 880 0 a440 440 0 1 0 -880 0 Z"/>
      <circle class="show-mark" cx="316" cy="180" r="92" fill="var(--lime)"/>
      <g class="chevrons" fill="none" stroke="var(--ink)" stroke-width="2.5">
        <polyline points="553,82 578,107 553,133"/>
        <polyline points="574,82 599,107 574,133"/>
        <polyline points="595,82 620,107 595,133"/>
        <polyline points="616,82 641,107 616,133"/>
        <polyline points="637,82 662,107 637,133"/>
      </g>
      <g class="triangles" fill="var(--ink)">
        <polygon points="341,632 376,610 376,655"/>
        <polygon points="361,632 396,610 396,655"/>
        <polygon points="381,632 416,610 416,655"/>
        <polygon points="401,632 436,610 436,655"/>
        <polygon points="421,632 456,610 456,655"/>
      </g>
      <g class="dots dots--ink" fill="var(--ink)">
        <circle cx="1103" cy="90" r="5"/><circle cx="1125" cy="90" r="5"/><circle cx="1147" cy="90" r="5"/>
        <circle cx="1103" cy="111" r="5"/><circle cx="1125" cy="111" r="5"/><circle cx="1147" cy="111" r="5"/>
        <circle cx="1103" cy="132" r="5"/><circle cx="1125" cy="132" r="5"/><circle cx="1147" cy="132" r="5"/>
        <circle cx="1103" cy="153" r="5"/><circle cx="1125" cy="153" r="5"/><circle cx="1147" cy="153" r="5"/>
        <circle cx="1103" cy="174" r="5"/><circle cx="1125" cy="174" r="5"/><circle cx="1147" cy="174" r="5"/>
        <circle cx="1103" cy="195" r="5"/><circle cx="1125" cy="195" r="5"/><circle cx="1147" cy="195" r="5"/>
        <circle cx="1103" cy="216" r="5"/><circle cx="1125" cy="216" r="5"/><circle cx="1147" cy="216" r="5"/>
      </g>
      <g class="dots dots--lime" fill="var(--lime)">
        <circle cx="5" cy="1076" r="5"/><circle cx="24" cy="1076" r="5"/>
        <circle cx="5" cy="1098" r="5"/><circle cx="24" cy="1098" r="5"/>
        <circle cx="5" cy="1120" r="5"/><circle cx="24" cy="1120" r="5"/>
        <circle cx="5" cy="1142" r="5"/><circle cx="24" cy="1142" r="5"/>
        <circle cx="5" cy="1164" r="5"/><circle cx="24" cy="1164" r="5"/>
      </g>
      <text class="podcast-label" transform="translate(255 1138) rotate(-90)"
        font-family="Oswald, sans-serif" font-weight="500" font-size="250"
        textLength="617" lengthAdjust="spacingAndGlyphs"
        fill="var(--paper)" stroke="var(--ink)" stroke-width="2.5">PODCAST</text>
    </g>
  </svg>

  <svg class="host-photo" width="1200" height="1200" viewBox="0 0 1200 1200" role="img" aria-label="Portrait photo of the podcast host in a dark blazer and white shirt, with blurred green foliage in the foreground">
    <defs>
      <linearGradient id="host-photo-tones" x1="0" y1="134" x2="0" y2="1200" gradientUnits="userSpaceOnUse">
        <stop offset="0" stop-color="var(--photo-top)"/>
        <stop offset="0.4" stop-color="var(--photo-top)"/>
        <stop offset="0.58" stop-color="var(--photo-mid)"/>
        <stop offset="1" stop-color="var(--photo-low)"/>
      </linearGradient>
    </defs>
    <path fill="url(#host-photo-tones)"
      d="M492 1200 V800 Q496 760 560 740 L650 700 V330 Q650 134 860 134 Q1070 134 1070 330 V600 Q1200 630 1200 700 V1200 Z"/>
  </svg>

  <h1 class="show-title">
    <span class="show-title__main">FORMOSAN</span>
    <span class="show-title__sub">TRAIL BLAZERS</span>
  </h1>
</main>
</body>
</html>
```